Brackenlow Rotors Business Card

We are a new company based in Central Queensland, Australia that uses specalised drones (Vantorq Sprayhawk K40) to undertake mainly agricultural operations, like spraying weeds, spraying crops, spreading seed etc. I have attached a Plimsy proof of a card I was thinking along the lines of - purely a start point. The drone used in the business card MUST be a Vantorq Sprayhawk K40.
I am very open to other ideas, especially fonts and layout. I don't have website etc set up yet.
The images are stock and easily interchangeable, I just ask that any background images reflect the local central Queensland area. The photo of the drone is not even complete (propellers cut off) and I need a new stock photo – I’m not sure if this is an issue, or I can pay for an image if need be. PLEASE FIND AN SPRAYHAWK K40 image - 4 sprayers, not 6.
The logo/business name is very draft and looking for further ideas, ideally incorporating drones or agriculture design elements into the design of the business name. The business name needs work on the graphic/design – it is a draft that I have included, the drone propellers (being a different colour) are DRAFT only and intended for changes. PLEASE DO NOT USE THE DRONE PORPELLER I HAVE USED AS A DRAFT. TRY TO FIND SOMETHING ELSE.. The arrow is a shape and not aligned in any way, I would also like ideas on different fonts and additional elements, like air streams, aviation elements, aviation or country western (farming like) themes and fonts etc.
Ideally looking at staying within the blue, green and yellow colours, keeping with an natural, outdoorsy, environmental feel.

Target Market(s)

Farmers, Agriculture, Local Governments, Land Managers

Industry/Entity Type

Agriculture, Drones, Aviation

Contact Information for Business Card

Agricultural Drone (Vantorq Sprayhawk K40), Farming, Business Name.

Font styles to use
Sans Serif

Colors
0054AA
0677BA
7BADD7
CADEEF
E8F1F8
0094D4
00A9DD
6FCCEA
C7EBF8
E9F6FB
00AB8E
00BBA5
67D7C9
C6EFE9
E9F9F6
59FF00
82FF00
B8FF75
E3FFCB
F4FFEA

Requirements
Must have
• Vantorq Sprayhawk K40 Drone
Should not have
• Tractors

```html
<!DOCTYPE html>
<html lang="en">
<head>
<meta charset="utf-8">
<title>Brackenlow Rotors Business Card</title>
<link href="https://fonts.googleapis.com/css2?family=Saira:wght@600;700&family=Poppins:wght@400;600&display=swap" rel="stylesheet">
<style>
  :root{
    --stage:#8a8a8a;
    --card:#ffffff;
    --green:#3a9a0f;
    --ink:#2a2a2a;
    --rule:#b9b9b9;
    --bar-grey:#acacac;
    --strip-field:#6f9f45;
    --strip-green:#3fa81c;
    --drone-light:#eceef0;
    --drone-mid:#d3d7db;
  }
  *{margin:0;padding:0;box-sizing:border-box}
  html,body{width:1200px;height:1200px;overflow:hidden}
  body{background:var(--stage);position:relative;font-family:"Poppins",sans-serif;color:var(--ink)}
  .card{position:absolute;left:162px;width:876px;height:500px;background:var(--card);overflow:hidden;box-shadow:6px 10px 14px rgba(0,0,0,.28)}
  .card--front{top:71px}
  .card--back{top:615px}

  /* front */
  .strip{position:absolute;top:0}
  .strip--field{background:var(--strip-field)}
  .strip--green{background:var(--strip-green)}
  .strip-1{left:49px;width:88px;height:308px}
  .strip-2{left:145px;width:87px;height:393px}
  .strip-3{left:240px;width:87px;height:348px}
  .strip-4{left:336px;width:88px;height:308px}

  .drone-photo{position:absolute;border-radius:28px;background:linear-gradient(160deg,var(--drone-light) 0%,var(--drone-mid) 100%)}
  .card--front .drone-photo{left:118px;top:165px;width:250px;height:180px}

  .brand{font-family:"Saira",sans-serif;font-weight:700;color:var(--ink);display:flex;align-items:center;line-height:.95;letter-spacing:-.5px}
  .brand__dot{flex:none;border-radius:50%;background:var(--green)}
  .card--front .brand{position:absolute;left:470px;top:130px;font-size:56px;gap:16px}
  .card--front .brand__dot{width:30px;height:30px}

  .services{position:absolute;left:504px;top:270px;list-style:none}
  .services li{display:flex;align-items:center;gap:14px;height:42px;font-family:"Saira",sans-serif;font-weight:700;font-size:25px;color:var(--ink)}
  .services svg{width:32px;height:32px;flex:none}
  .front-url{position:absolute;left:467px;top:420px;font-size:22px;letter-spacing:1.2px;color:var(--ink)}
  .front-url b{color:var(--green);font-weight:600}

  /* back */
  .bar{position:absolute;top:0}
  .bar--grey{left:613px;width:81px;height:340px;background:var(--bar-grey)}
  .bar--green{left:707px;width:81px;height:340px;background:var(--green)}
  .card--back .drone-photo{left:520px;top:150px;width:250px;height:175px}
  .card--back .brand{position:absolute;left:79px;top:70px;font-size:40px;gap:12px}
  .card--back .brand__dot{width:22px;height:22px}
  .person{position:absolute;left:79px;top:214px}
  .person__name{font-family:"Saira",sans-serif;font-weight:700;font-size:52px;line-height:1;color:var(--ink)}
  .person__name span{color:var(--green)}
  .person__role{font-size:31px;letter-spacing:1.5px;margin-top:8px;color:var(--ink)}
  .divider{position:absolute;left:79px;top:340px;width:628px;height:1px;background:var(--rule)}
  .contact{position:absolute;display:flex;align-items:center;gap:9px;font-size:21px;color:var(--ink);white-space:nowrap}
  .contact svg{width:22px;height:22px;flex:none}
  .c-phone{left:79px;top:366px}
  .c-mail{left:79px;top:406px}
  .c-pin{left:466px;top:366px}
  .c-web{left:466px;top:406px}
</style>
</head>
<body>

<section class="card card--front">
  <div class="strips" role="img" aria-label="Aerial photo of green Central Queensland farmland under blue sky, cut into four vertical strips">
    <div class="strip strip--field strip-1"></div>
    <div class="strip strip--green strip-2"></div>
    <div class="strip strip--field strip-3"></div>
    <div class="strip strip--green strip-4"></div>
  </div>
  <div class="drone-photo" role="img" aria-label="Photo of a Vantorq Sprayhawk K40 agricultural spray drone in flight"></div>

  <div class="brand"><span class="brand__dot"></span><span>Brackenlow<br>Rotors</span></div>

  <ul class="services">
    <li>
      <svg viewBox="0 0 32 32"><circle cx="16" cy="16" r="16" fill="#3a9a0f"/><path d="M16 7c-3 4-3 8 0 13 3-5 3-9 0-13zM8 12c1 5 4 8 8 8-1-4-4-7-8-8zm16 0c-4 1-7 4-8 8 4 0 7-3 8-8zM16 20v5" fill="#fff" stroke="#fff" stroke-width="1.2"/></svg>
      Spraying Weeds
    </li>
    <li>
      <svg viewBox="0 0 32 32"><circle cx="16" cy="16" r="16" fill="#3a9a0f"/><g fill="none" stroke="#fff" stroke-width="1.8" stroke-linecap="round"><path d="M11 25V10M16 25V8M21 25V10"/><path d="M11 14l-2-2M11 18l-2-2M11 14l2-2M11 18l2-2M16 12l-2-2M16 16l-2-2M16 12l2-2M16 16l2-2M21 14l-2-2M21 18l-2-2M21 14l2-2M21 18l2-2"/></g></svg>
      Spraying Crops
    </li>
    <li>
      <svg viewBox="0 0 32 32"><circle cx="16" cy="16" r="16" fill="#3a9a0f"/><path d="M16 24V15" stroke="#fff" stroke-width="2"/><path d="M16 16c-1-4-4-6-8-6 0 4 3 6 8 6zm0-2c1-4 4-6 8-6 0 4-3 6-8 6z" fill="#fff"/><path d="M10 24h12" stroke="#fff" stroke-width="2" stroke-linecap="round"/></svg>
      Spreading Seed
    </li>
  </ul>

  <p class="front-url">www.<b>brackenlowrotors</b>.com.au</p>
</section>

<section class="card card--back">
  <div class="bar bar--grey"></div>
  <div class="bar bar--green"></div>
  <div class="drone-photo" role="img" aria-label="Photo of a Vantorq Sprayhawk K40 agricultural spray drone seen from below"></div>

  <div class="brand"><span class="brand__dot"></span><span>Brackenlow<br>Rotors</span></div>

  <div class="person">
    <h1 class="person__name"><span>Dale</span> Merrow</h1>
    <p class="person__role">Founder</p>
  </div>

  <div class="divider"></div>

  <p class="contact c-phone">
    <svg viewBox="0 0 24 24"><path d="M6 2l3 5-2 2c1 3 4 6 7 7l2-2 5 3-2 4C10 21 3 14 2 5z" fill="#3a9a0f"/></svg>
    012.555.0148
  </p>
  <p class="contact c-mail">
    <svg viewBox="0 0 24 24"><rect x="1" y="5" width="22" height="14" fill="#3a9a0f"/><path d="M1 5l11 8 11-8M1 19l8-7M23 19l-8-7" fill="none" stroke="#fff" stroke-width="1.5"/></svg>
    hello@brackenlowrotors.com.au
  </p>
  <p class="contact c-pin">
    <svg viewBox="0 0 24 24"><path d="M12 1a8 8 0 0 0-8 8c0 6 8 14 8 14s8-8 8-14a8 8 0 0 0-8-8z" fill="#3a9a0f"/><circle cx="12" cy="9" r="3" fill="#fff"/></svg>
    48 Kelso Road, Emerald
  </p>
  <p class="contact c-web">
    <svg viewBox="0 0 24 24"><circle cx="12" cy="12" r="10" fill="none" stroke="#3a9a0f" stroke-width="2"/><path d="M2 12h20M12 2c-4 5-4 15 0 20M12 2c4 5 4 15 0 20M4 7h16M4 17h16" fill="none" stroke="#3a9a0f" stroke-width="1.5"/></svg>
    www.brackenlowrotors.com.au
  </p>
</section>

</body>
</html>
```